Create American style design suitable for consumers in Europe and America

We need a professional universal neutral design, which can be applied to all personal care tools, regardless of male and female, and the color matching needs to be matched by designers themselves.
Updates

设计质量低

Target Market(s)

Europe and America

Industry/Entity Type

personal care tools

Font styles to use
Serif
Sans Serif
Script

Requirements
Must have
• personal beauty care tool,like nail clipper,tweezer,scissors
Nice to have
• The copywriter plans on the packaging design can be applied to all personal care tools
Should not have
• Not designed for a single product, but for a whole personal care tool

```html
<!DOCTYPE html>
<html lang="en">
<head>
<meta charset="utf-8">
<title>Kalia Everyday Care – Nail Clipper Packaging</title>
<link rel="stylesheet" href="https://fonts.googleapis.com/css2?family=Hind:wght@300;400;500;600&family=Oswald:wght@500&display=swap">
<style>
  :root{
    --board:#231f20;
    --board-edge:#000000;
    --ink:#1f1f1f;
    --gold:#d2a94f;
    --gold-soft:#f5ecd9;
    --teal:#3fa48a;
    --teal-deep:#9fd8d4;
    --teal-base:#cdf1e8;
    --dots-orange:#f0a546;
    --dots-peach:#f9dcc0;
    --dots-mint:#c9e8e2;
    --hole:#231f20;
  }
  *{box-sizing:border-box;margin:0;padding:0}
  html,body{width:1200px;height:715px;overflow:hidden;background:#ffffff}
  body{position:relative;font-family:"Hind",sans-serif;color:var(--ink)}

  .board{position:absolute;width:321px;height:268px;background:var(--board)}
  .board--framed{background:var(--board-edge);width:316px;height:267px}
  .board--framed::before{content:"";position:absolute;left:14px;top:13px;right:14px;bottom:14px;background:var(--board)}

  .card{position:absolute;width:136px;height:227px;border-radius:5px;overflow:hidden;--s:1;text-align:center;background:#fff}
  .card--small{width:121px;height:203px;--s:.89}
  .card::after{content:"";position:absolute;left:0;right:0;bottom:0;height:4px;background:var(--accent)}

  .theme-gold{--accent:var(--gold);--head:var(--gold)}
  .theme-teal{--accent:var(--teal);--head:var(--teal)}
  .theme-dots{--accent:var(--dots-orange);--head:var(--teal)}

  .card__pattern{position:absolute;inset:0}
  .theme-gold .card__pattern{background:radial-gradient(circle at 30% 30%,#ffffff 0,var(--gold-soft) 60%,#fbf7ee 100%)}
  .theme-teal .card__pattern{background:
      radial-gradient(circle at 10% 12%,var(--teal-deep) 0 28%,transparent 29%),
      radial-gradient(circle at 100% 40%,var(--teal-deep) 0 22%,transparent 23%),
      radial-gradient(circle at 95% 95%,var(--teal-deep) 0 26%,transparent 27%),
      var(--teal-base)}
  .theme-dots .card__pattern{background:linear-gradient(160deg,#fdf2e6 0%,#ffffff 45%,#eef7f5 100%)}

  .card__hole{position:absolute;left:50%;top:4%;width:24px;height:7px;margin-left:-12px;border-radius:4px;background:var(--hole)}
  .card__hole::before{content:"";position:absolute;left:50%;top:-3px;width:8px;height:8px;margin-left:-4px;border-radius:50%;background:var(--hole)}

  .brand{position:absolute;left:0;right:0;top:9.5%;line-height:1}
  .brand__name{font-weight:400;font-size:calc(19px * var(--s));letter-spacing:.5px;color:var(--ink)}
  .brand__tag{display:block;font-weight:400;font-size:calc(6px * var(--s));margin-top:1px;color:var(--ink)}

  .title{position:absolute;left:0;right:0;font-weight:600;font-size:calc(17px * var(--s));line-height:1;color:var(--head);letter-spacing:.2px}
  .subtitle{position:absolute;left:0;right:0;font-weight:400;font-size:calc(7.6px * var(--s));line-height:1;color:var(--ink)}
  .card--front .title{top:83%}
  .card--front .subtitle{top:90.5%}
  .card--back .title{top:24.5%}
  .card--back .subtitle{top:33%}

  .copy{position:absolute;left:10%;right:10%;top:39.5%;font-size:calc(4.1px * var(--s));line-height:1.3;text-align:justify;text-align-last:center;color:var(--ink)}
  .theme-dots .copy{left:8%;right:8%;top:38%;padding:3px 4px 14px;border:1px solid #f3d3ad;border-radius:5px}

  .badges{position:absolute;left:0;right:0;top:68.5%;display:flex;justify-content:center;gap:calc(9px * var(--s))}
  .badge{width:calc(26px * var(--s));height:calc(26px * var(--s));border-radius:50%;background:#fff;border:1px solid #c9c9c9;box-shadow:0 0 0 1px #fff,0 0 0 2px #d8d8d8;display:flex;align-items:center;justify-content:center;font-family:"Oswald",sans-serif;font-weight:500;font-size:calc(3.6px * var(--s));line-height:1.15;color:var(--ink)}

  .contact{position:absolute;left:0;right:0;top:84%;font-size:calc(4.8px * var(--s));line-height:1.45;color:var(--ink)}
  .contact__ask{color:var(--accent);text-transform:uppercase}
  .theme-teal .contact__ask{color:var(--teal)}
  .card--small .contact, .board--rich .contact{font-weight:600}

  .product{position:absolute;left:50%;width:52px;margin-left:-26px;top:23%;height:55%;border-radius:26px 26px 10px 10px;background:linear-gradient(180deg,#b9b9b9 0%,#8a8a8a 22%,#2b2b2b 40%,#1a1a1a 100%);opacity:.9}
</style>
</head>
<body>

<!-- Board 1: gold, plain -->
<section class="board" style="left:45px;top:74px">
  <article class="card card--front theme-gold" style="left:19px;top:20px">
    <div class="card__pattern" role="img" aria-label="Soft cream pattern of overlapping circles"></div>
    <div class="card__hole"></div>
    <div class="brand"><span class="brand__name">kalia</span><span class="brand__tag">Everyday Care</span></div>
    <h2 class="title">NAIL CLIPPER</h2>
    <p class="subtitle">Personal beauty care tool</p>
  </article>
  <article class="card card--back theme-gold" style="left:164px;top:20px">
    <div class="card__pattern" role="img" aria-label="Soft cream pattern of overlapping circles"></div>
    <div class="card__hole"></div>
    <div class="brand"><span class="brand__name">kalia</span><span class="brand__tag">Everyday Care</span></div>
    <h2 class="title">NAIL CLIPPER</h2>
    <p class="subtitle">Personal beauty care tool</p>
    <p class="copy">Crafted for everyday grooming, this tool is made from hardened stainless steel with a precise edge that stays sharp through years of use. The balanced grip offers steady control for trimming, shaping and tidying at home or on the go. Rinse after use, dry thoroughly and store in a cool place to keep it in top condition for every member of the family.</p>
    <div class="badges"><div class="badge">High<br>Quality<br>Stainless<br>Steel</div><div class="badge">100%<br>Satisfaction<br>Guaranteed</div></div>
    <div class="contact"><div class="contact__ask">Any questions? Contact us</div><div>PH: (555) 214-0398</div><div>E: hello@kaliacare.com</div><div>W: www.kaliacare.com</div></div>
  </article>
</section>

<!-- Board 2: teal, plain -->
<section class="board" style="left:438px;top:74px">
  <article class="card card--front theme-teal" style="left:19px;top:20px">
    <div class="card__pattern" role="img" aria-label="Mint background with soft teal blob shapes"></div>
    <div class="card__hole"></div>
    <div class="brand"><span class="brand__name">kalia</span><span class="brand__tag">Everyday Care</span></div>
    <h2 class="title">NAIL CLIPPER</h2>
    <p class="subtitle">Personal beauty care tool</p>
  </article>
  <article class="card card--back theme-teal" style="left:164px;top:20px">
    <div class="card__pattern" role="img" aria-label="Mint background with soft teal blob shapes"></div>
    <div class="card__hole"></div>
    <div class="brand"><span class="brand__name">kalia</span><span class="brand__tag">Everyday Care</span></div>
    <h2 class="title">NAIL CLIPPER</h2>
    <p class="subtitle">Personal beauty care tool</p>
    <p class="copy">Crafted for everyday grooming, this tool is made from hardened stainless steel with a precise edge that stays sharp through years of use. The balanced grip offers steady control for trimming, shaping and tidying at home or on the go. Rinse after use, dry thoroughly and store in a cool place to keep it in top condition for every member of the family.</p>
    <div class="badges"><div class="badge">High<br>Quality<br>Stainless<br>Steel</div><div class="badge">100%<br>Satisfaction<br>Guaranteed</div></div>
    <div class="contact"><div class="contact__ask">Any questions? Contact us</div><div>PH: (555) 214-0398</div><div>E: hello@kaliacare.com</div><div>W: www.kaliacare.com</div></div>
  </article>
</section>

<!-- Board 3: dots, plain -->
<section class="board" style="left:840px;top:74px">
  <article class="card card--front theme-dots" style="left:19px;top:20px">
    <div class="card__pattern" role="img" aria-label="Peach and mint polka dot pattern"></div>
    <div class="card__hole"></div>
    <div class="brand"><span class="brand__name">kalia</span><span class="brand__tag">Everyday Care</span></div>
    <h2 class="title">NAIL CLIPPER</h2>
    <p class="subtitle">Personal beauty care tool</p>
  </article>
  <article class="card card--back theme-dots" style="left:164px;top:20px">
    <div class="card__pattern" role="img" aria-label="Peach and mint polka dot pattern"></div>
    <div class="card__hole"></div>
    <div class="brand"><span class="brand__name">kalia</span><span class="brand__tag">Everyday Care</span></div>
    <h2 class="title">NAIL CLIPPER</h2>
    <p class="subtitle">Personal beauty care tool</p>
    <p class="copy">Crafted for everyday grooming, this tool is made from hardened stainless steel with a precise edge that stays sharp through years of use. The balanced grip offers steady control for trimming, shaping and tidying at home or on the go. Rinse after use, dry thoroughly and store in a cool place to keep it in top condition for every member of the family.</p>
    <div class="badges"><div class="badge">High<br>Quality<br>Stainless<br>Steel</div><div class="badge">100%<br>Satisfaction<br>Guaranteed</div></div>
    <div class="contact"><div class="contact__ask">Any questions? Contact us</div><div>PH: (555) 214-0398</div><div>E: hello@kaliacare.com</div><div>W: www.kaliacare.com</div></div>
  </article>
</section>

<!-- Board 4: gold, with product -->
<section class="board board--framed" style="left:47px;top:358px">
  <article class="card card--small card--front theme-gold" style="left:31px;top:31px">
    <div class="card__pattern" role="img" aria-label="Soft cream pattern of overlapping circles"></div>
    <div class="card__hole"></div>
    <div class="brand"><span class="brand__name">kalia</span><span class="brand__tag">Everyday Care</span></div>
    <div class="product" role="img" aria-label="Photo of a stainless steel nail clipper with black handles"></div>
    <h2 class="title">NAIL CLIPPER</h2>
    <p class="subtitle">Personal beauty care tool</p>
  </article>
  <article class="card card--small card--back theme-gold" style="left:161px;top:31px">
    <div class="card__pattern" role="img" aria-label="Soft cream pattern of overlapping circles"></div>
    <div class="card__hole"></div>
    <div class="brand"><span class="brand__name">kalia</span><span class="brand__tag">Everyday Care</span></div>
    <h2 class="title">NAIL CLIPPER</h2>
    <p class="subtitle">Personal beauty care tool</p>
    <p class="copy">Crafted for everyday grooming, this tool is made from hardened stainless steel with a precise edge that stays sharp through years of use. The balanced grip offers steady control for trimming, shaping and tidying at home or on the go. Rinse after use, dry thoroughly and store in a cool place to keep it in top condition for every member of the family.</p>
    <div class="badges"><div class="badge">High<br>Quality<br>Stainless<br>Steel</div><div class="badge">100%<br>Satisfaction<br>Guaranteed</div></div>
    <div class="contact"><div class="contact__ask">Any questions? Contact us</div><div>PH: (555) 214-0398</div><div>E: hello@kaliacare.com</div><div>W: www.kaliacare.com</div></div>
  </article>
</section>

<!-- Board 5: teal, with product -->
<section class="board board--rich" style="left:438px;top:358px">
  <article class="card card--front theme-teal" style="left:19px;top:20px">
    <div class="card__pattern" role="img" aria-label="Mint background with soft teal blob shapes"></div>
    <div class="card__hole"></div>
    <div class="brand"><span class="brand__name">kalia</span><span class="brand__tag">Everyday Care</span></div>
    <div class="product" role="img" aria-label="Photo of a stainless steel nail clipper with black handles"></div>
    <h2 class="title">NAIL CLIPPER</h2>
    <p class="subtitle">Personal beauty care tool</p>
  </article>
  <article class="card card--back theme-teal" style="left:164px;top:20px">
    <div class="card__pattern" role="img" aria-label="Mint background with soft teal blob shapes"></div>
    <div class="card__hole"></div>
    <div class="brand"><span class="brand__name">kalia</span><span class="brand__tag">Everyday Care</span></div>
    <h2 class="title">NAIL CLIPPER</h2>
    <p class="subtitle">Personal beauty care tool</p>
    <p class="copy">Crafted for everyday grooming, this tool is made from hardened stainless steel with a precise edge that stays sharp through years of use. The balanced grip offers steady control for trimming, shaping and tidying at home or on the go. Rinse after use, dry thoroughly and store in a cool place to keep it in top condition for every member of the family.</p>
    <div class="badges"><div class="badge">High<br>Quality<br>Stainless<br>Steel</div><div class="badge">100%<br>Satisfaction<br>Guaranteed</div></div>
    <div class="contact"><div class="contact__ask">Any questions? Contact us</div><div>PH: (555) 214-0398</div><div>E: hello@kaliacare.com</div><div>W: www.kaliacare.com</div></div>
  </article>
</section>

<!-- Board 6: dots, with product -->
<section class="board board--rich" style="left:840px;top:353px;height:267px">
  <article class="card card--front theme-dots" style="left:19px;top:20px">
    <div class="card__pattern" role="img" aria-label="Peach and mint polka dot pattern"></div>
    <div class="card__hole"></div>
    <div class="brand"><span class="brand__name">kalia</span><span class="brand__tag">Everyday Care</span></div>
    <div class="product" role="img" aria-label="Photo of a stainless steel nail clipper with black handles"></div>
    <h2 class="title">NAIL CLIPPER</h2>
    <p class="subtitle">Personal beauty care tool</p>
  </article>
  <article class="card card--back theme-dots" style="left:164px;top:20px">
    <div class="card__pattern" role="img" aria-label="Peach and mint polka dot pattern"></div>
    <div class="card__hole"></div>
    <div class="brand"><span class="brand__name">kalia</span><span class="brand__tag">Everyday Care</span></div>
    <h2 class="title">NAIL CLIPPER</h2>
    <p class="subtitle">Personal beauty care tool</p>
    <p class="copy">Crafted for everyday grooming, this tool is made from hardened stainless steel with a precise edge that stays sharp through years of use. The balanced grip offers steady control for trimming, shaping and tidying at home or on the go. Rinse after use, dry thoroughly and store in a cool place to keep it in top condition for every member of the family.</p>
    <div class="badges"><div class="badge">High<br>Quality<br>Stainless<br>Steel</div><div class="badge">100%<br>Satisfaction<br>Guaranteed</div></div>
    <div class="contact"><div class="contact__ask">Any questions? Contact us</div><div>PH: (555) 214-0398</div><div>E: hello@kaliacare.com</div><div>W: www.kaliacare.com</div></div>
  </article>
</section>

</body>
</html>
```